Business Card for premium dental clinic

We are a premium dental clinic based in Brasov, Romania with more than 15 year on the market, providing quality dental treatment made by a team of more specialized dentists, working with modern equipment as a solution to beautiful and healthy teeth.

Our current logo for the clinic use 2 square with colors black and gold - dr Corbescu - studio, using family fonts Bodoni, Myriad Pro and Segoe Print.
Depending on the printing we used some gold CMYK background or gold foil picture background or a gold gradient.
We want a business card:
- eye catching business card
- distinguished business card
- premium design
- to keep the color scheme of black and gold
- to attract the customers to spent time reading the information
- modern concept

```html
<!DOCTYPE html>
<html lang="en">
<head>
<meta charset="utf-8">
<title>Nordvale Dental Clinic – Business Card</title>
<link rel="stylesheet" href="https://fonts.googleapis.com/css2?family=Encode+Sans+Condensed:wght@400;500&family=Montserrat:wght@400;500;600&display=swap">
<style>
  :root {
    --backdrop: #2a211d;
    --card: #333436;
    --card-gloss: #111213;
    --gold: #c9a04c;
    --gold-light: #e3c27a;
  }
  * { box-sizing: border-box; margin: 0; padding: 0; }
  html, body {
    width: 1200px;
    height: 800px;
    overflow: hidden;
    background: var(--backdrop);
  }
  .canvas {
    position: relative;
    width: 1200px;
    height: 800px;
  }
  .card {
    position: absolute;
    width: 520px;
    height: 298px;
    background: var(--card);
    border: 2px solid var(--gold);
    border-radius: 3px;
    box-shadow: 0 12px 30px rgba(0, 0, 0, 0.45);
  }
  .card--front { left: 70px; top: 90px; }
  .card--back { left: 610px; top: 412px; }

  .clinic-name {
    position: absolute;
    left: 0;
    right: 0;
    top: 50%;
    transform: translateY(-50%);
    text-align: center;
    font-family: "Montserrat", sans-serif;
    font-weight: 600;
    font-size: 32px;
    letter-spacing: 0.5px;
    color: var(--card-gloss);
  }

  .doctor {
    position: absolute;
    left: 40px;
    top: 124px;
    font-family: "Encode Sans Condensed", sans-serif;
    font-weight: 500;
    font-size: 44px;
    line-height: 1;
    white-space: nowrap;
    color: var(--gold);
  }
  .doctor__title { font-size: 26px; margin-right: 4px; }

  .divider {
    position: absolute;
    left: 262px;
    top: 96px;
    width: 1.5px;
    height: 104px;
    background: var(--gold);
  }

  .contacts {
    position: absolute;
    left: 280px;
    top: 112px;
    list-style: none;
    font-family: "Montserrat", sans-serif;
    font-size: 12.5px;
    line-height: 24px;
    white-space: nowrap;
    color: var(--gold-light);
  }
  .contacts li { display: flex; align-items: center; gap: 8px; }
  .contacts .icon { width: 12px; height: 12px; flex: none; fill: var(--gold); }
</style>
</head>
<body>
<main class="canvas">
  <section class="card card--front" aria-label="Card front">
    <p class="clinic-name">Nordvale Dental Clinic</p>
  </section>

  <section class="card card--back" aria-label="Card back">
    <h1 class="doctor"><span class="doctor__title">dr.</span>Corbescu</h1>
    <div class="divider"></div>
    <ul class="contacts">
      <li>
        <svg class="icon" viewBox="0 0 24 24" aria-hidden="true"><path d="M6.6 10.8a15.1 15.1 0 0 0 6.6 6.6l2.2-2.2a1 1 0 0 1 1-.25 11.4 11.4 0 0 0 3.6.57 1 1 0 0 1 1 1V20a1 1 0 0 1-1 1A17 17 0 0 1 3 4a1 1 0 0 1 1-1h3.5a1 1 0 0 1 1 1c0 1.25.2 2.45.57 3.57a1 1 0 0 1-.25 1z"/></svg>
        +40 268 555 210
      </li>
      <li>
        <svg class="icon" viewBox="0 0 24 24" aria-hidden="true"><path d="M2 5h20v14H2z M3.5 6.5l8.5 6.5 8.5-6.5" fill="none" stroke="#c9a04c" stroke-width="2"/></svg>
        contact@nordvaledental.ro
      </li>
      <li>
        <svg class="icon" viewBox="0 0 24 24" aria-hidden="true"><circle cx="12" cy="12" r="10" fill="none" stroke="#c9a04c" stroke-width="2.5"/><path d="M2 12h20M12 2c3 3 3 17 0 20M12 2c-3 3-3 17 0 20" fill="none" stroke="#c9a04c" stroke-width="1.8"/></svg>
        www.nordvaledental.ro
      </li>
    </ul>
  </section>
</main>
</body>
</html>
```